I need business cards for a company that will be an umbrella for many retail stores. I need them to be sleek and modern. I would like some white and black in the background of the card as these are the office colours the logo is attached.
Target Market(s)
worldwide
Industry/Entity Type
Business
Requirements
Must have
- traditional business card shape
Should not have
- too many colours
no swirly text

```html
<!DOCTYPE html>
<html lang="en">
<head>
<meta charset="utf-8">
<title>Norvale General Trading – Business Card</title>
<link rel="stylesheet" href="https://fonts.googleapis.com/css2?family=Tinos&family=Noto+Sans&display=swap">
<style>
  :root {
    --card-white: #ffffff;
    --ink: #111111;
    --ink-soft: #2a2a2a;
    --brand-blue: #1b6db5;
    --ghost-text: rgba(150, 150, 150, 0.28);
    --wave-dark: #1c1c1c;
    --wave-mid: #8a8a8a;
    --wave-light: #ffffff;
  }
  html, body {
    margin: 0;
    padding: 0;
    width: 1200px;
    height: 686px;
    overflow: hidden;
    background: var(--card-white);
  }
  .card {
    position: relative;
    width: 1200px;
    height: 686px;
    overflow: hidden;
    background: var(--card-white);
    font-family: "Tinos", "Times New Roman", serif;
    color: var(--ink);
  }
  .card__wave {
    position: absolute;
    inset: 0;
    width: 1200px;
    height: 686px;
  }
  .brand {
    position: absolute;
    left: 92px;
    top: 150px;
    display: flex;
    align-items: center;
    gap: 22px;
  }
  .brand__dot {
    width: 46px;
    height: 46px;
    border-radius: 50%;
    background: var(--brand-blue);
    flex: none;
  }
  .brand__name {
    font-family: "Tinos", "Times New Roman", serif;
    font-weight: 400;
    color: var(--ink-soft);
    text-transform: uppercase;
    letter-spacing: 2px;
    line-height: 1.05;
    font-size: 27px;
  }
  .brand__name span { display: block; }
  .brand__name .brand__line--main { font-size: 38px; }
  .ghost-name {
    position: absolute;
    left: 500px;
    top: 255px;
    font-family: "Tinos", "Times New Roman", serif;
    font-weight: 400;
    text-transform: uppercase;
    color: var(--ghost-text);
    line-height: 1;
    white-space: nowrap;
  }
  .ghost-name span { display: block; }
  .ghost-name .ghost-name__main { font-size: 112px; letter-spacing: 6px; }
  .ghost-name .ghost-name__sub { font-size: 84px; letter-spacing: 3px; margin-top: 20px; }
  .person {
    position: absolute;
    left: 518px;
    top: 318px;
    width: 200px;
    text-align: center;
    line-height: 1;
  }
  .person__name { font-size: 42px; display: block; }
  .person__title { font-size: 31px; display: block; margin-top: -3px; }
  .business-description {
    position: absolute;
    left: 70px;
    top: 512px;
    font-family: "Noto Sans", Tahoma, sans-serif;
    font-size: 42px;
    color: var(--ink);
    letter-spacing: -0.5px;
  }
  .contact {
    position: absolute;
    right: 73px;
    top: 490px;
    text-align: right;
    font-size: 36px;
    line-height: 42px;
    color: var(--ink);
  }
  .contact span { display: block; }
</style>
</head>
<body>
  <div class="card">
    <svg class="card__wave" viewBox="0 0 1200 686" aria-hidden="true">
      <defs>
        <linearGradient id="waveShade" x1="520" y1="686" x2="1180" y2="0" gradientUnits="userSpaceOnUse">
          <stop offset="0" stop-color="var(--wave-dark)"/>
          <stop offset="0.5" stop-color="var(--wave-mid)"/>
          <stop offset="1" stop-color="var(--wave-light)"/>
        </linearGradient>
      </defs>
      <path d="M1017,0 C900,80 740,180 754,300 C762,360 790,375 762,430 C705,540 600,625 486,686 L1200,686 L1200,0 Z" fill="url(#waveShade)"/>
    </svg>

    <div class="ghost-name" aria-hidden="true">
      <span class="ghost-name__main">Norvale</span>
      <span class="ghost-name__sub">General Trading</span>
    </div>

    <div class="brand">
      <span class="brand__dot"></span>
      <div class="brand__name">
        <span class="brand__line--main">Norvale</span>
        <span>General Trading</span>
      </div>
    </div>

    <div class="person">
      <span class="person__name">Name</span>
      <span class="person__title">Title</span>
    </div>

    <div class="business-description">Business Description</div>

    <div class="contact">
      <span>Website</span>
      <span>Email</span>
      <span>Phone</span>
    </div>
  </div>
</body>
</html>
```